An insurance broker wants to represent the company's vision visually and textually.

My company, with a total of 10 employees, developed a vision this year. Now, we want to display this vision in the form of a two-meter-high visual that will be mounted on the wall. This ensures that the vision is always visible to our employees, as well as to our clients and partners when they visit our office.

Here's my idea: the vision will be accompanied by a fitting image, with the text of the vision itself elegantly written in a beautiful font. Our vision reads: "Every company always has a perfectly tailored future solution for greater financial security, freedom, and joy."

A bit about my company: we are an insurance broker, and our services are primarily designed for corporate clients.

```html
<!DOCTYPE html>
<html lang="en">
<head>
<meta charset="utf-8">
<title>Vision — Every Company Always Has a Perfectly Tailored Future Solution</title>
<link rel="stylesheet" href="https://fonts.googleapis.com/css2?family=Saira+Condensed:wght@700;800&display=swap">
<style>
  :root {
    --paper: #ededeb;
    --ink: #0b0b0b;
    --sky: #03a2f4;
    --stone: #9d9d9d;
  }
  html, body {
    margin: 0;
    padding: 0;
    width: 1200px;
    height: 685px;
    overflow: hidden;
    background: var(--paper);
  }
  .vision {
    display: block;
    width: 1200px;
    height: 685px;
  }
  .vision text {
    font-family: "Saira Condensed", "Arial Narrow", sans-serif;
    font-weight: 800;
  }
  .ink { fill: var(--ink); }
  .sky { fill: var(--sky); }
  .stone { fill: var(--stone); }
  .placeholder-smile { fill: var(--sky); opacity: 0.35; }
  .placeholder-umbrella { fill: var(--ink); opacity: 0.85; }
  .placeholder-birds { fill: var(--ink); opacity: 0.85; }
</style>
</head>
<body>
<svg class="vision" viewBox="0 0 1200 685" xmlns="http://www.w3.org/2000/svg" aria-labelledby="vision-title">
  <title id="vision-title">Every company always has a perfectly tailored future solution for greater financial security, freedom, and joy.</title>
  <rect width="1200" height="685" fill="var(--paper)"/>

  <!-- decorative areas -->
  <rect class="placeholder-smile" role="img" aria-label="Simple blue smiling emoticon" x="496" y="71" width="104" height="75" rx="37"/>
  <rect class="placeholder-umbrella" role="img" aria-label="Black umbrella silhouette" x="233" y="212" width="92" height="99" rx="46"/>
  <rect class="placeholder-birds" role="img" aria-label="Two black birds flying upward" x="930" y="376" width="152" height="120" rx="20"/>

  <!-- vision wording -->
  <text class="stone" x="621" y="154" font-size="86" textLength="190" lengthAdjust="spacingAndGlyphs">EVERY</text>
  <text class="ink" x="404" y="246" font-size="113" textLength="407" lengthAdjust="spacingAndGlyphs">COMPANY</text>
  <text class="sky" transform="translate(877 247) rotate(-90)" x="0" y="0" font-size="63" textLength="174" lengthAdjust="spacingAndGlyphs">ALWAYS</text>
  <text class="ink" transform="translate(383 400) rotate(-90)" x="0" y="0" font-size="64" textLength="226" lengthAdjust="spacingAndGlyphs">TAILORED</text>
  <text class="stone" x="226" y="348" font-size="46" textLength="94" lengthAdjust="spacingAndGlyphs">HAS A</text>
  <text class="stone" x="146" y="395" font-size="47" textLength="174" lengthAdjust="spacingAndGlyphs">PERFECTLY</text>
  <text class="sky" x="405" y="400" font-size="189" textLength="517" lengthAdjust="spacingAndGlyphs">FUTURE</text>
  <text class="sky" x="143" y="546" font-size="189" textLength="665" lengthAdjust="spacingAndGlyphs">SOLUTION</text>
  <text class="ink" x="829" y="480" font-size="58" textLength="91" lengthAdjust="spacingAndGlyphs">FOR</text>
  <text class="ink" x="828" y="550" font-size="63" textLength="212" lengthAdjust="spacingAndGlyphs">GREATER</text>
  <text x="145" y="616" font-size="50" textLength="911" lengthAdjust="spacingAndGlyphs" xml:space="preserve"><tspan class="ink">FINANCIAL </tspan><tspan class="sky">SECURITY,</tspan><tspan class="ink">   FREEDOM, AND </tspan><tspan class="sky">JOY.</tspan></text>
</svg>
</body>
</html>
```